Vice chair

I'm running for a position as vice chair this will be posted in the lunch room cafeteria in this package i posted logos, my picture, sample of old flyers to give you a idea i also wrote literature need help in putting it together like it to look like a million bucks goal win this election I summited lots of pdf files and jpeg look though them to help with your design feel free to contact me to further assist you
Updates

Would like this to be completed by Wednesday

Target Market(s)

My constituents

Font styles to use
Serif

Colors

Designer to choose colors to be used in the design.

Requirements
Must have
• Make it look clean neat
Nice to have
• Nice background

```html
<!DOCTYPE html>
<html lang="en">
<head>
<meta charset="utf-8">
<title>Vice Chair Campaign Flyer</title>
<link href="https://fonts.googleapis.com/css2?family=Anton&family=Bebas+Neue&family=Carlito:wght@400;700&display=swap" rel="stylesheet">
<style>
  :root{
    --stage:#4d4d4d;
    --paper:#ffffff;
    --red:#ec1f27;
    --ink:#1c1c1c;
    --rule:#555555;
    --mist:#e9e9ea;
    --black:#000000;
  }
  *{box-sizing:border-box;margin:0;padding:0}
  html,body{width:1200px;height:1200px;overflow:hidden;background:var(--stage)}
  .flyer{
    position:absolute;left:240px;top:90px;width:721px;height:1020px;
    background:var(--paper);overflow:hidden;
    font-family:"Carlito","Calibri",sans-serif;color:var(--ink);
  }
  .backdrop{position:absolute;left:0;top:0;width:721px;height:470px}
  .headline{
    position:absolute;left:0;top:22px;width:100%;text-align:center;
    font-family:"Anton",sans-serif;color:#fff;font-size:68px;line-height:1;letter-spacing:0.5px;
  }
  .subhead{
    position:absolute;left:0;top:103px;width:100%;
    display:flex;justify-content:center;align-items:center;gap:14px;
    font-family:"Bebas Neue",sans-serif;color:#fff;font-size:50px;line-height:1;
  }
  .subhead .line{width:144px;height:2px;background:#fff}
  .portrait{
    position:absolute;left:200px;top:163px;width:296px;height:296px;border-radius:50%;
    background:radial-gradient(circle at 50% 40%,#8a6a58 0%,#5b4338 38%,#d9d6d6 70%);
  }
  .intro{
    position:absolute;left:19px;top:470px;width:684px;
    font-size:13px;line-height:17.6px;
  }
  .intro p{margin-bottom:11px;text-align:justify}
  .experiences{
    position:absolute;left:18px;top:626px;width:685px;height:140px;
    border:1.5px solid var(--rule);border-radius:3px;
  }
  .experiences-tab{
    position:absolute;left:278px;top:609px;width:167px;height:43px;
    background:var(--red);color:#fff;text-align:center;
    font-family:"Bebas Neue",sans-serif;font-size:28px;line-height:45px;
  }
  .exp-item{position:absolute;font-size:13px;line-height:17.6px;text-align:center}
  .exp-years{left:29px;top:46px;font-size:21px;line-height:23px;font-weight:700;text-align:left}
  .exp-local-a{left:205px;top:46px;width:240px}
  .exp-local-b{left:472px;top:47px;width:200px}
  .closing{
    position:absolute;left:30px;top:780px;width:660px;text-align:center;
    font-size:13px;line-height:17.6px;
  }
  .vote-bar{
    position:absolute;left:0;top:840px;width:100%;height:50px;background:var(--red);
    color:#fff;text-align:center;font-family:"Bebas Neue",sans-serif;font-size:37px;line-height:54px;
  }
  .depots{
    position:absolute;left:0;top:925px;width:100%;height:50px;
    display:flex;justify-content:center;gap:52px;align-items:center;
  }
  .depot{display:flex;align-items:center;gap:8px;font-size:14px;font-weight:700;color:var(--ink)}
  .depot-dot{width:22px;height:22px;border-radius:50%;background:var(--red)}
  .base-strip{position:absolute;left:0;bottom:0;width:100%;height:15px;background:var(--black)}
</style>
</head>
<body>
  <main class="flyer">
    <svg class="backdrop" viewBox="0 0 721 470" aria-hidden="false">
      <defs>
        <linearGradient id="mist" x1="0" y1="0" x2="1" y2="1">
          <stop offset="0" stop-color="#ececec"/>
          <stop offset="0.5" stop-color="#f7f7f7"/>
          <stop offset="1" stop-color="#e6e6e6"/>
        </linearGradient>
      </defs>
      <rect role="img" aria-label="Faded voting sticker and flag background" x="0" y="120" width="721" height="350" fill="url(#mist)"/>
      <rect x="0" y="420" width="721" height="50" fill="#fff" opacity="0.7"/>
      <path d="M0 0 H721 V100 C660 200 560 260 460 255 L240 255 C150 255 60 230 0 135 Z" fill="var(--red)"/>
    </svg>

    <h1 class="headline">TIME FOR CHANGE</h1>
    <div class="subhead"><span class="line"></span><span>VOTE THE SLATE</span><span class="line"></span></div>

    <div class="portrait" role="img" aria-label="Portrait photo of the candidate"></div>

    <section class="intro">
      <p>I <strong>Marcus Delgado</strong> for those who don’t know me would like to introduce myself I have always been approachable and helpful whether you are a probationary officer or a veteran operator with knowledge or information. we must protect our union rules for ourselves our future and most important our children.</p>
      <p>I would like this oppurtunity to run as your vice chair a person you can trust and believe in me . Positive and motivations are my main keys for progress and for change in my campaign when there are no leaders to look up to one therefore must become one. I do believe I’m the right person for this position so please come out and support me and vote me as your vice chair.</p>
    </section>

    <section class="experiences">
      <div class="exp-item exp-years">20 years<br>on the job</div>
      <div class="exp-item exp-local-a">Past Union member of Freightworkers local 412 belives in ,there is a collective bargaining agreement in place and no management is above the law to violate it.</div>
      <div class="exp-item exp-local-b">Past union member of freightworkers local 736 believes a house that is divided cannot be stand alone</div>
    </section>
    <div class="experiences-tab">MY EXPERIENCES</div>

    <p class="closing">In closing I believe that our union does not stand out individually achievement we must stand out collective advancement for all. We must always continue to stand together, stay together &amp; fight together so we can win together because success is never owned, it is rented and the rent is due every day.</p>

    <div class="vote-bar">VOTE INDEPENDENT ME AS YOUR VICE CHAIR</div>

    <div class="depots">
      <div class="depot"><span class="depot-dot"></span>Millbrook Depot</div>
      <div class="depot"><span class="depot-dot"></span>Cedar Ridge Depot</div>
      <div class="depot"><span class="depot-dot"></span>Harbor Point Depot</div>
    </div>

    <div class="base-strip"></div>
  </main>
</body>
</html>
```